App Design for FlavorRoam

We need an app design for a new app called FlavorRoam, which is an app designed to inspire exploration through personalized recipe generation, local restaurant discoveries, and a vibrant community platform. It caters to food enthusiasts looking to explore global cuisines or find the best local dining spots, offering a premium experience with selected features available for free.

-------UPDATED-----
This app will be AI Driven and may not be heavily dependent on media (images,videos) at first, especially for the Recipe generator feature. Our goal is to still have attractive UI. The core functionalities we are looking are the following
1. Recipe Generator: Either user choose a specific cuisine(italian,spanish), or user inputs ingredients and get recipe, or get recipe for different occasions (xmas, thanksgiving ) and get a randomly get recipe to cook, plain simple. We expect the recipes to be displayed in clear and not too generic manner starting with ingredients and expected duration at top and then step by step guide. We also intend to enable premium users to have playful action button or icon to get unlimited recipes generated until they find what they like and also have save for later feature. These premium features should be disabled for free users and prompted to subscribe if they click them with nice popup
2. Restaurant Recommendation - will have selected pictures and will be based on inputs such as zip code and other filters such as cousine types. Premium users can filter by price range, get unlimited recommendation, see actual price range in the recommendation and can save for later where they can find it later. Free users cannot filter by price (disabled) and should see it hidden in the recommendation
3. Meal Planning - will include just simple and random meal plan with just one button or limited interaction for free, users need to subscribe to get features such as customized plan such as considering allergies or diet preferences. Premium users can also get a shopping checklist of ingredients for weekly meal preps and their step by step guide for each meal recipe.
2. Community Sharing: users can view posts and engage with community content
Updates

Hello Designers,

The initial price was not fair for the work. So I have increased it. There will also be $50-100 bonus for those who come up with great designs or for those who incorporate interesting stuff. Thank you! Much appreciated 🙏

Colors
0054AA
0677BA
7BADD7
CADEEF
E8F1F8
0094D4
00A9DD
6FCCEA
C7EBF8
E9F6FB
00AB8E
00BBA5
67D7C9
C6EFE9
E9F9F6
FFC000
F8CF3A
FAE287
FDF2CF
FEFAEE
F0912C
F2A743
F7CA91
FBE8D2
FDF5EE
EE7325
F08F49
F5BC92
FAE3D3
FDF4ED
A7469A
B969AE
D3A5CF
EDDBEB
F8F0F9
6B429C
8869AF
B7A5CE
E3DAEB
F3F0F8

```html
<!DOCTYPE html>
<html lang="en">
<head>
<meta charset="utf-8">
<title>FlavorRoam – Restaurant</title>
<link href="https://fonts.googleapis.com/css2?family=Figtree:wght@400;500;600;700&display=swap" rel="stylesheet">
<style>
:root{
  --bg:#FBF9F6;
  --ink:#2E3A47;
  --ink-soft:#3A3F45;
  --muted:#9A9A9A;
  --accent:#FC7149;
  --field:#FDF3E3;
  --field-ring:#ECEAC6;
  --tip:#FFF0D4;
  --tip-border:#F0D698;
  --card:#FEF6EC;
  --status:#000;
}
*{box-sizing:border-box;margin:0;padding:0}
html,body{width:1200px;height:2847px;overflow:hidden;background:var(--bg);font-family:"Figtree",sans-serif;color:var(--ink)}
.screen{position:relative;width:1200px;height:2847px;overflow:hidden;background:var(--bg)}
.abs{position:absolute}
.status-bar{left:0;top:0;width:1200px;height:134px;background:var(--status);border-radius:70px 70px 0 0;color:#fff}
.status-bar .time{position:absolute;left:73px;top:40px;font-size:44px;font-weight:600}
.avatar{left:45px;top:167px;width:134px;height:134px;border-radius:50%;background:radial-gradient(circle at 50% 40%,#c58a6a,#6a4b3c 55%,#7a5fa3)}
.menu-btn{left:1021px;top:167px;width:134px;height:134px;border-radius:50%;background:var(--accent)}
.heading{left:45px;top:403px;font-size:45px;font-weight:600;color:var(--ink)}
.field{left:45px;width:1110px;height:144px;border-radius:72px;background:var(--field);font-size:39px;color:var(--ink-soft);display:flex;align-items:center;padding-left:45px}
.field-ring{left:45px;width:1110px;height:188px;border-radius:94px;border:2px solid var(--field-ring)}
.field-ring .field{left:20px;top:20px;width:1066px;padding-left:45px}
.locked{filter:blur(1.6px);opacity:.8}
.pill{height:143px;border-radius:72px;background:var(--field);font-size:39px;color:var(--ink-soft);display:flex;align-items:center;justify-content:center}
.tip{border:2px solid var(--tip-border);background:var(--tip);border-radius:48px;display:flex;align-items:center;gap:26px;padding-left:56px;font-size:34px;font-weight:500;line-height:1.2;color:#1E1E1E}
.cta{left:45px;top:1462px;width:1110px;height:157px;border-radius:79px;background:var(--accent);color:#fff;font-size:45px;font-weight:700;display:flex;align-items:center;justify-content:center;gap:20px}
.section-title{left:45px;top:1767px;font-size:45px;font-weight:600}
.card{top:1842px;height:655px;border-radius:56px;background:var(--card);overflow:hidden}
.card .photo{position:absolute;left:0;top:0;width:100%;height:328px;background:linear-gradient(120deg,#8a5a35,#c9a27a 40%,#6b3a22 75%,#3e2216)}
.card .info{position:absolute;left:45px;top:365px;filter:blur(1.8px)}
.card .name{font-size:50px;font-weight:700;color:#444}
.card .addr{font-size:33px;color:#777;margin-top:18px}
.card .meta{display:flex;gap:80px;font-size:34px;color:#666;margin-top:56px}
.tabbar{left:0;top:2647px;width:1200px;height:200px;border-top:2px solid #F0EEEA;background:var(--bg)}
.tab{position:absolute;top:36px;width:240px;margin-left:-120px;text-align:center;font-size:33px;font-weight:500;color:#B3B3B3}
.tab svg{display:block;margin:0 auto 14px}
.tab.active{color:var(--accent)}
</style>
</head>
<body>
<div class="screen">
  <header class="abs status-bar">
    <span class="time">9:41</span>
    <svg class="abs" style="left:956px;top:44px" width="62" height="46" viewBox="0 0 62 46" fill="none" stroke="#fff" stroke-width="5" stroke-linecap="round"><path d="M4 16a38 38 0 0 1 54 0"/><path d="M14 26a24 24 0 0 1 34 0"/><path d="M24 36a10 10 0 0 1 14 0"/></svg>
    <svg class="abs" style="left:1063px;top:48px" width="62" height="38" viewBox="0 0 62 38" fill="none"><rect x="3" y="3" width="50" height="32" rx="9" stroke="#fff" stroke-width="4"/><rect x="13" y="12" width="5" height="14" rx="2" fill="#fff"/><rect x="22" y="12" width="5" height="14" rx="2" fill="#fff"/><rect x="55" y="13" width="5" height="12" rx="2" fill="#fff"/></svg>
  </header>

  <div class="abs avatar" role="img" aria-label="User profile photo"></div>
  <svg class="abs" style="left:925px;top:203px" width="58" height="62" viewBox="0 0 58 62" fill="none" stroke="#FC7149" stroke-width="4" stroke-linejoin="round"><path d="M6 18l12 12 11-20 11 20 12-12-5 34H11z"/><circle cx="29" cy="40" r="3" fill="#FC7149"/></svg>
  <div class="abs menu-btn">
    <svg class="abs" style="left:40px;top:44px" width="54" height="46" viewBox="0 0 54 46" stroke="#fff" stroke-width="4" stroke-linecap="round"><path d="M4 6h46M4 23h46M4 40h30"/></svg>
  </div>

  <h1 class="abs heading">Let’s get you a place to eat</h1>

  <div class="abs field" style="top:481px">Enter Zip code</div>
  <div class="abs field-ring" style="top:649px"><div class="abs field">Choose&nbsp; Couisine type</div></div>
  <div class="abs field-ring" style="top:861px"><div class="abs field">Choose different occasions</div></div>

  <div class="locked">
    <div class="abs field" style="top:1073px">Max Distance</div>
    <div class="abs field-ring" style="top:1240px">
      <div class="abs pill" style="left:20px;top:21px;width:262px">Min Price</div>
      <div class="abs pill" style="left:307px;top:21px;width:279px">Max Price</div>
    </div>
  </div>
  <div class="abs tip" style="left:325px;top:1151px;width:553px;height:148px;padding-left:56px">
    <svg width="56" height="62" viewBox="0 0 56 62" fill="none" stroke="#FC7149" stroke-width="4" stroke-linecap="round"><path d="M16 26V17a12 12 0 0 1 23-4"/><rect x="5" y="26" width="46" height="32" rx="10"/><path d="M28 37v9"/></svg>
    <span>Go premium to unlock<br>these features</span>
  </div>

  <div class="abs cta">
    <svg width="58" height="58" viewBox="0 0 58 58" fill="none" stroke="#fff" stroke-width="4" stroke-linecap="round" stroke-linejoin="round"><path d="M20 24l32 32M16 28l8-8"/><path d="M32 4l3 7 7 3-7 3-3 7-3-7-7-3 7-3z"/><path d="M8 8v8M4 12h8M10 40v8M6 44h8"/></svg>
    Get your restaurant
  </div>

  <h2 class="abs section-title">Nearby Restaurant</h2>

  <div class="abs card" style="left:-40px;width:132px"><div class="photo" role="img" aria-label="Restaurant interior photo"></div></div>
  <article class="abs card" style="left:114px;width:826px">
    <div class="photo" role="img" aria-label="Warm wooden restaurant dining room photo"></div>
    <div class="info">
      <div class="name">Pizza Restaurant 01</div>
      <div class="addr">Address 1234 N St</div>
      <div class="meta"><span style="color:#666"><b style="color:#FC7149">★</b> 4.2 (30+)</span><span>◎ 2.5 Km</span><span>◉ 25-300</span></div>
    </div>
  </article>
  <article class="abs card" style="left:963px;width:300px">
    <div class="photo" role="img" aria-label="Bright restaurant interior photo" style="background:linear-gradient(120deg,#e8e4dc,#8a6a4c 50%,#d9d3c8)"></div>
    <div class="info">
      <div class="name">Pizza Re</div>
      <div class="addr">Address 123</div>
      <div class="meta"><span><b style="color:#FC7149">★</b> 4.2 (30+</span></div>
    </div>
  </article>
  <div class="abs tip" style="left:253px;top:2097px;width:552px;height:148px">
    <svg width="56" height="62" viewBox="0 0 56 62" fill="none" stroke="#FC7149" stroke-width="4" stroke-linecap="round"><path d="M16 26V17a12 12 0 0 1 23-4"/><rect x="5" y="26" width="46" height="32" rx="10"/><path d="M28 37v9"/></svg>
    <span>Go premium to unlock<br>these features</span>
  </div>

  <nav class="abs tabbar">
    <div class="tab" style="left:173px"><svg width="60" height="64" viewBox="0 0 60 64" fill="none" stroke="#B3B3B3" stroke-width="4" stroke-linecap="round"><rect x="5" y="5" width="50" height="54" rx="12"/><path d="M18 26h24M18 38h14"/></svg>Recipes</div>
    <div class="tab active" style="left:458px"><svg width="60" height="64" viewBox="0 0 60 64" fill="none" stroke="#FC7149" stroke-width="4" stroke-linecap="round" stroke-linejoin="round"><rect x="6" y="12" width="48" height="48" rx="8"/><path d="M22 4l8 8 8-8"/><path d="M18 44h24M18 36l12-10 12 10"/></svg>Restaurant</div>
    <div class="tab" style="left:741px"><svg width="64" height="64" viewBox="0 0 64 64" fill="none" stroke="#B3B3B3" stroke-width="4" stroke-linecap="round"><path d="M6 34h52a26 16 0 0 1-52 0z"/><path d="M14 34a18 16 0 0 1 36 0"/><path d="M24 22l6 6 8-10"/></svg>Meal</div>
    <div class="tab" style="left:1024px"><svg width="64" height="64" viewBox="0 0 64 64" fill="none" stroke="#B3B3B3" stroke-width="4" stroke-linecap="round"><circle cx="26" cy="20" r="11"/><path d="M6 56c0-12 9-20 20-20s20 8 20 20z"/><path d="M40 10a11 11 0 0 1 0 20M48 38c6 3 10 9 10 18"/></svg>Comm</div>
  </nav>
</div>
</body>
</html>
```